Business Card Design Project

We require a business card template to cover basic contact information - our company logo, names of employees, title, mobile and email.

Target Market(s)

Corporate

Industry/Entity Type

Business

Font styles to use
Sans Serif

Requirements
Nice to have
• Thinking it would be great just to have the logo taking up approximately half the space (so it goes as far across the top of the card as possible) and then contact details in the lower half of the card. Keen just to use only the two colours in the logo, on a white background.
Should not have
• No fussy drawings

```html
<!DOCTYPE html>
<html lang="en">
<head>
<meta charset="utf-8">
<title>Tidewell Developments – Business Card</title>
<link href="https://fonts.googleapis.com/css2?family=PT+Sans:wght@400;700&display=swap" rel="stylesheet">
<style>
  :root {
    --page: #e9ebee;
    --card-white: #f7f8fa;
    --brand-blue: #1f4f9e;
    --brand-navy: #1b3b7c;
    --brand-teal: #1e9aa9;
    --back-blue: #2f5b95;
  }
  * { margin: 0; padding: 0; box-sizing: border-box; }
  html, body {
    width: 1200px; height: 723px; overflow: hidden;
    background: var(--page);
    font-family: "PT Sans", sans-serif;
  }
  .canvas { position: relative; width: 1200px; height: 723px; }

  .card {
    position: absolute; top: 81px;
    width: 330px; height: 560px;
    overflow: hidden;
    box-shadow: 0 6px 18px rgba(0,0,0,0.15);
  }

  /* Back side */
  .card--back { left: 220px; background: var(--back-blue); }
  .back-wordmark {
    position: absolute; left: 50%; top: 50%;
    transform: translate(-50%, -50%) rotate(90deg);
    white-space: nowrap; text-align: right;
    color: var(--brand-teal);
  }
  .back-wordmark .name { display: block; font-size: 130px; line-height: 0.9; font-weight: 400; }
  .back-wordmark .sub { display: block; font-size: 36px; line-height: 1; font-weight: 400; }

  /* Front side */
  .card--front { left: 650px; background: var(--card-white); }
  .edge-band {
    position: absolute; top: 0; right: 0; width: 20px; height: 100%;
    background: var(--brand-blue);
  }
  .base-band {
    position: absolute; left: 0; bottom: 0; right: 20px; height: 16px;
    background: var(--brand-teal);
  }
  .logo {
    position: absolute; top: 22px; right: 40px; text-align: right;
    color: var(--brand-teal); font-weight: 400;
  }
  .logo .name { display: block; font-size: 54px; line-height: 1; }
  .logo .sub { display: block; font-size: 15px; line-height: 1; margin-top: 2px; }

  .person {
    position: absolute; top: 210px; left: 36px;
    color: var(--brand-navy); font-size: 26px; letter-spacing: 0.5px;
  }
  .contact {
    position: absolute; top: 290px; left: 36px; right: 40px;
    list-style: none; color: var(--brand-teal);
    font-size: 17px; line-height: 1.5; letter-spacing: 0;
    white-space: nowrap;
  }
  .website {
    position: absolute; bottom: 34px; left: 36px;
    color: var(--brand-teal); font-size: 24px; letter-spacing: 0.5px;
  }
</style>
</head>
<body>
  <main class="canvas">
    <section class="card card--back" aria-label="Card back">
      <div class="back-wordmark">
        <span class="name">Tidewell</span>
        <span class="sub">developments</span>
      </div>
    </section>

    <section class="card card--front" aria-label="Card front">
      <div class="logo">
        <span class="name">Tidewell</span>
        <span class="sub">developments</span>
      </div>
      <p class="person">YOUR NAME</p>
      <ul class="contact">
        <li>XXXXXX XXXXXXX XXXXXX</li>
        <li>PH : 402-718-316</li>
        <li>EMAIL : HELLO@TIDEWELL.COM</li>
      </ul>
      <p class="website">WWW.TIDEWELL.COM</p>
      <div class="base-band"></div>
      <div class="edge-band"></div>
    </section>
  </main>
</body>
</html>
```